Health & Wellness Contest - The Bright Harvest Renewal

We need a postcard design that is professional and grabs the attention of people who see it. The postcard will be left in fitness centers and posted on social media. The front of the card MUST look amazing - make potential participants want to pick it up and find out more information; the back of the card will have the contest details. The goal is to have people sign up for a 90 day fitness program, and most of the marketing will be with this postcard.

Target Market(s)

People that are thinking about beginning a health regiment; people who are already used to exercising and are willing to try a new supplement

Industry/Entity Type

Health And Wellness

Colors

Designer to choose colors to be used in the design.

Requirements
Must have
• Front Cover -- Must have the phrase "The Bright Harvest Renewal" and must have "$2,500 Grand Prize"; and must have "BrightHarvestRenewal.com"
Nice to have
• Design on Front; Details on Back; appeal to both men and women

```html
<!DOCTYPE html>
<html lang="en">
<head>
<meta charset="utf-8">
<title>The Bright Harvest Renewal – Postcard</title>
<link href="https://fonts.googleapis.com/css2?family=Michroma&family=Oswald:wght@600&family=Lato:wght@400&display=swap" rel="stylesheet">
<style>
  :root {
    --blue-deep: #123a8c;
    --blue-mid: #1f56b8;
    --blue-light: #3f7fe0;
    --white: #ffffff;
    --band: #f1f3f6;
    --ink-blue: #1f4fae;
    --backdrop: #8c8c8c;
    --line-grey: #9a9a9a;
  }
  * { box-sizing: border-box; margin: 0; padding: 0; }
  html, body { width: 1200px; height: 1200px; overflow: hidden; }
  body { background: var(--backdrop); position: relative; font-family: "Lato", sans-serif; }

  .card { position: absolute; left: 288px; width: 624px; height: 486px; overflow: hidden;
    box-shadow: 0 4px 10px rgba(0,0,0,.35); }
  .card--front { top: 40px;
    background: linear-gradient(160deg, var(--blue-deep) 0%, var(--blue-mid) 45%, var(--blue-light) 60%, var(--blue-mid) 75%, var(--blue-deep) 100%); }
  .card--back { top: 612px; background: var(--white); }

  .front__photo { position: absolute; left: 360px; top: 0; width: 264px; height: 486px;
    background: linear-gradient(200deg, rgba(196,140,100,0) 0%, rgba(176,120,84,.85) 35%, rgba(150,100,70,.9) 65%, rgba(40,80,170,.9) 100%); }

  .front__title { position: absolute; left: 16px; top: 22px; font-family: "Michroma", sans-serif;
    color: var(--white); line-height: 1.25; text-shadow: 0 2px 3px rgba(0,0,0,.45); z-index: 2; }
  .front__title .line1 { display: block; font-size: 30px; }
  .front__title .line2 { display: block; font-size: 38px; }
  .front__mission { position: absolute; left: 16px; top: 130px; width: 420px; font-family: "Michroma", sans-serif;
    color: var(--white); font-size: 13px; line-height: 23px; z-index: 2; }

  .prize-band { position: absolute; left: 0; top: 190px; width: 440px; height: 104px;
    background: linear-gradient(90deg, var(--band) 0%, var(--band) 80%, rgba(241,243,246,0) 100%); z-index: 1; }
  .prize-band__trophy { position: absolute; left: 20px; top: 10px; width: 72px; height: 86px; }
  .prize-band__amount { position: absolute; left: 130px; top: 4px; font-family: "Michroma", sans-serif;
    font-size: 44px; color: var(--ink-blue); }
  .prize-band__label { position: absolute; left: 106px; top: 66px; font-family: "Michroma", sans-serif;
    font-size: 27px; color: var(--ink-blue); }

  .front__visit { position: absolute; left: 16px; top: 300px; font-family: "Michroma", sans-serif;
    font-size: 17px; color: var(--white); z-index: 2; }
  .front__url { position: absolute; left: 0; top: 330px; width: 296px; height: 32px; background: var(--band);
    color: var(--ink-blue); font-size: 23px; line-height: 32px; padding-left: 16px; z-index: 2; }

  .front__sponsor { position: absolute; left: 16px; top: 388px; width: 230px; text-align: center;
    color: var(--white); z-index: 2; }
  .front__sponsor .mark { display: block; width: 34px; height: 34px; margin: 0 auto 10px; background: var(--white); }
  .front__sponsor .name { font-family: "Lato", sans-serif; font-size: 17px; letter-spacing: 1px; line-height: 1.3; }

  .back__panel { position: absolute; inset: 0; }
  .back__heading { position: absolute; left: 15px; top: 22px; width: 300px; font-family: "Oswald", sans-serif;
    font-weight: 600; font-size: 16px; line-height: 21px; color: var(--white); }
  .benefits { position: absolute; left: 15px; top: 96px; list-style: none; }
  .benefits li { display: flex; align-items: center; height: 28px; color: var(--white); font-size: 19px; }
  .benefits svg { width: 18px; height: 18px; margin-right: 10px; flex: none; }
  .deadline { position: absolute; left: 0; top: 352px; width: 284px; height: 52px; background: rgba(10,40,110,.45);
    color: var(--white); padding-left: 46px; }
  .deadline small { display: block; font-size: 15px; padding-top: 5px; }
  .deadline strong { display: block; font-weight: 400; font-size: 27px; line-height: 28px; }
  .contact { position: absolute; left: 20px; display: flex; align-items: center; color: var(--white); font-size: 14.5px; white-space: nowrap; }
  .contact svg { width: 16px; height: 16px; margin-right: 10px; flex: none; }
  .contact--mail { top: 412px; }
  .contact--web { top: 440px; }
  .stamp { position: absolute; left: 516px; top: 14px; width: 95px; height: 95px; border: 1.5px solid #222; }
  .address-line { position: absolute; left: 352px; width: 234px; height: 1px; background: var(--line-grey); }
</style>
</head>
<body>

<section class="card card--front">
  <div class="front__photo" role="img" aria-label="Photo of an athlete curling a barbell"></div>
  <h1 class="front__title"><span class="line1">THE BRIGHT HARVEST</span><span class="line2">RENEWAL</span></h1>
  <p class="front__mission">THE BRIGHT HARVEST RENEWAL HAS ONE MISSION – TO HELP PEOPLE BE A BETTER</p>
  <div class="prize-band">
    <svg class="prize-band__trophy" viewBox="0 0 72 86" aria-hidden="true">
      <path d="M14 4h44v14c0 16-9 28-22 30C23 46 14 34 14 18z" fill="#2a5cc0"/>
      <path d="M14 10H4c0 14 6 22 14 24M58 10h10c0 14-6 22-14 24" fill="none" stroke="#2a5cc0" stroke-width="4"/>
      <rect x="32" y="48" width="8" height="18" fill="#2a5cc0"/>
      <rect x="20" y="66" width="32" height="14" rx="2" fill="#2a5cc0"/>
    </svg>
    <div class="prize-band__amount">$2,500</div>
    <div class="prize-band__label">GRAND PRIZE</div>
  </div>
  <p class="front__visit">VISIT US</p>
  <p class="front__url">BrightHarvestRenewal.com</p>
  <div class="front__sponsor">
    <span class="mark"></span>
    <span class="name">KEYSTONE<br>Legal Partners</span>
  </div>
</section>

<section class="card card--back">
  <svg class="back__panel" viewBox="0 0 624 486" preserveAspectRatio="none" aria-hidden="true">
    <defs>
      <linearGradient id="panelFill" x1="0" y1="0" x2="1" y2="1">
        <stop offset="0" stop-color="#123a8c"/>
        <stop offset=".45" stop-color="#1f56b8"/>
        <stop offset=".6" stop-color="#3f7fe0"/>
        <stop offset="1" stop-color="#123a8c"/>
      </linearGradient>
    </defs>
    <polygon points="0,0 346,0 272,486 0,486" fill="url(#panelFill)"/>
  </svg>
  <h2 class="back__heading">JOIN US IN THE BRIGHT HARVEST RENEWAL AND EXPERIENCE SOME OF THE BENEFITS THAT COUNTLESS OTHERS HAVE SEEN:</h2>
  <ul class="benefits">
    <li><svg viewBox="0 0 18 18"><circle cx="9" cy="9" r="8" fill="none" stroke="#fff" stroke-width="1.5"/><path d="M7 5l4 4-4 4" fill="none" stroke="#fff" stroke-width="1.8"/></svg>Better health</li>
    <li><svg viewBox="0 0 18 18"><circle cx="9" cy="9" r="8" fill="none" stroke="#fff" stroke-width="1.5"/><path d="M7 5l4 4-4 4" fill="none" stroke="#fff" stroke-width="1.8"/></svg>Appetite suppression</li>
    <li><svg viewBox="0 0 18 18"><circle cx="9" cy="9" r="8" fill="none" stroke="#fff" stroke-width="1.5"/><path d="M7 5l4 4-4 4" fill="none" stroke="#fff" stroke-width="1.8"/></svg>Better energy</li>
    <li><svg viewBox="0 0 18 18"><circle cx="9" cy="9" r="8" fill="none" stroke="#fff" stroke-width="1.5"/><path d="M7 5l4 4-4 4" fill="none" stroke="#fff" stroke-width="1.8"/></svg>Fat Loss</li>
    <li><svg viewBox="0 0 18 18"><circle cx="9" cy="9" r="8" fill="none" stroke="#fff" stroke-width="1.5"/><path d="M7 5l4 4-4 4" fill="none" stroke="#fff" stroke-width="1.8"/></svg>Better focus</li>
    <li><svg viewBox="0 0 18 18"><circle cx="9" cy="9" r="8" fill="none" stroke="#fff" stroke-width="1.5"/><path d="M7 5l4 4-4 4" fill="none" stroke="#fff" stroke-width="1.8"/></svg>Increased awareness</li>
    <li><svg viewBox="0 0 18 18"><circle cx="9" cy="9" r="8" fill="none" stroke="#fff" stroke-width="1.5"/><path d="M7 5l4 4-4 4" fill="none" stroke="#fff" stroke-width="1.8"/></svg>Better mood</li>
    <li><svg viewBox="0 0 18 18"><circle cx="9" cy="9" r="8" fill="none" stroke="#fff" stroke-width="1.5"/><path d="M7 5l4 4-4 4" fill="none" stroke="#fff" stroke-width="1.8"/></svg>Muscle preservation</li>
    <li><svg viewBox="0 0 18 18"><circle cx="9" cy="9" r="8" fill="none" stroke="#fff" stroke-width="1.5"/><path d="M7 5l4 4-4 4" fill="none" stroke="#fff" stroke-width="1.8"/></svg>Better sleep</li>
  </ul>
  <div class="deadline">
    <small>Challenge Deadline: Register by</small>
    <strong>October 31, 2017</strong>
  </div>
  <p class="contact contact--mail"><svg viewBox="0 0 18 18"><rect x="1" y="4" width="16" height="11" fill="#fff"/><path d="M1 4l8 6 8-6" fill="none" stroke="#1f56b8" stroke-width="1.5"/></svg>Info@KeystoneLegal.org</p>
  <p class="contact contact--web"><svg viewBox="0 0 18 18"><circle cx="9" cy="9" r="8" fill="none" stroke="#fff" stroke-width="1.4"/><ellipse cx="9" cy="9" rx="3.5" ry="8" fill="none" stroke="#fff" stroke-width="1.2"/><path d="M1 9h16M2.5 5h13M2.5 13h13" stroke="#fff" stroke-width="1.2"/></svg>www.BrightHarvestRenewal.com</p>
  <div class="stamp"></div>
  <div class="address-line" style="top:344px"></div>
  <div class="address-line" style="top:382px"></div>
  <div class="address-line" style="top:419px"></div>
</section>

</body>
</html>
```